Design a Website for Brivoln Consulting

Hi Friends,

I'm looking for a website design/build for [url removed, login to view] we are a consulting firm operating in the Asia-Pacific Region. Wordpress is ok- can pretty much emulate (imgae) one or combination of the below examples.

The design needs to be clean and user friendly with a sharp and professional look. Some examples of great sites we like are:

- [url removed, login to view] **

- [url removed, login to view]

I look forward to seeing some great work.

Cheers

N

```html
<!DOCTYPE html>
<html lang="en">
<head>
<meta charset="utf-8">
<title>Brivoln Consulting</title>
<link rel="stylesheet" href="https://fonts.googleapis.com/css2?family=Source+Sans+3:wght@300;400;600&family=Montserrat:wght@400;600;700&family=Lora:wght@400&display=swap">
<style>
:root{
  --red:#ee1c25;
  --ink:#333538;
  --muted:#6f7379;
  --icon:#5f6470;
  --light:#f7f7f7;
  --gray:#f5f5f6;
  --cta:#f0f4f8;
  --footer:#131315;
  --footer-base:#0b0b0c;
}
*{margin:0;padding:0;box-sizing:border-box}
html,body{width:1200px;height:3709px;overflow:hidden}
body{position:relative;background:#fff;font-family:"Montserrat",sans-serif;color:var(--ink)}
.abs{position:absolute}
.center{left:0;width:1200px;text-align:center}

.topbar{top:0;left:0;width:1200px;height:40px;background:var(--light)}
.topbar .links{left:96px;top:13px;font-size:8px;letter-spacing:.5px;color:#999}
.topbar .links span{margin-right:14px}
.topbar .social{right:96px;top:12px;display:flex;gap:12px}
.dot{width:12px;height:12px;border-radius:50%;background:#8a8d92}

.header{top:40px;left:0;width:1200px;height:118px;background:#fff}
.brand{left:100px;top:42px;display:flex;align-items:center;gap:10px;font-weight:700;font-size:20px;letter-spacing:2px;color:var(--red)}
.brand .mark{width:28px;height:28px;border-radius:50%;background:var(--ink)}
.nav{top:52px;font-family:"Lora",serif;font-size:13px;letter-spacing:1px;color:#555}
.nav.active{color:var(--red)}
.search{left:1076px;top:45px;width:28px;height:28px;border:1.5px solid #ccc;border-radius:50%}

.hero{top:158px;left:0;width:1200px;height:542px;background:linear-gradient(180deg,#e9d3bb 0%,#caa682 35%,#7b6352 65%,#3d3230 100%)}
.hero h1{top:150px;font-family:"Source Sans 3",sans-serif;font-weight:300;font-size:72px;color:#2b2b2b;letter-spacing:-1px}
.hero p{top:228px;font-family:"Source Sans 3",sans-serif;font-size:19px;color:#2f2f2f}
.btn-red{background:var(--red);color:#fff;font-weight:600;font-size:11px;letter-spacing:2px;display:flex;align-items:center;justify-content:center}
.hero .btn-red{left:443px;top:304px;width:305px;height:48px}

.card-img{top:815px;width:304px;height:203px}
.card-title{top:1050px;font-weight:600;font-size:15px;letter-spacing:.5px;color:#222}
.card-text{top:1080px;width:300px;font-size:13px;line-height:22px;color:#666}

.features{top:1236px;left:0;width:1200px;height:835px;background:var(--gray)}
.features h2{top:76px;font-family:"Source Sans 3",sans-serif;font-weight:300;font-size:35px;color:#444}
.features .lead{top:124px;font-size:14px;line-height:25px;color:#666}
.feature{width:300px;text-align:center}
.feature svg{display:block;margin:0 auto}
.feature h3{margin-top:26px;font-family:"Source Sans 3",sans-serif;font-weight:300;font-size:26px;color:#555}
.feature p{margin:18px auto 0;width:250px;font-size:12px;line-height:20px;letter-spacing:.5px;color:#666}

.about-band{top:2071px;left:0;width:1200px;height:622px;background:linear-gradient(120deg,#e8c9a5 0%,#eab27e 45%,#d7a27a 70%,#b3a198 100%)}
.about-band h2{left:272px;top:136px;font-family:"Source Sans 3",sans-serif;font-weight:300;font-size:48px;color:#3a3532;letter-spacing:-1px}
.about-band h4{left:272px;top:204px;font-family:"Source Sans 3",sans-serif;font-size:18px;font-weight:400;color:#3a3532}
.about-band p{left:272px;top:240px;width:390px;font-family:"Source Sans 3",sans-serif;font-size:15px;line-height:26px;color:#9a7a62}
.call{left:272px;top:388px;display:flex;gap:14px}
.call strong{display:block;font-family:"Source Sans 3",sans-serif;font-weight:600;font-size:14px;color:#3a3532}
.call span{display:block;margin-top:6px;font-size:12px;color:#9a7a62;letter-spacing:.5px}

.cta{top:2693px;left:0;width:1200px;height:285px;background:var(--cta)}
.cta h2{top:60px;font-family:"Source Sans 3",sans-serif;font-weight:300;font-size:34px;line-height:40px;color:#444}
.btn-ghost{left:400px;top:186px;width:219px;height:40px;border:1px solid #c9ccd0;background:#fff;font-weight:600;font-size:11px;letter-spacing:2px;color:#333;display:flex;align-items:center;justify-content:center}
.cta .btn-red{left:648px;top:186px;width:151px;height:40px}

.partners{top:2978px;left:0;width:1200px;height:503px;background:#fff}
.partners h5{top:122px;font-weight:600;font-size:15px;letter-spacing:2px;color:#333}
.partners .rule{left:582px;top:150px;width:36px;height:2px;background:var(--red)}
.partners p{top:192px;font-family:"Source Sans 3",sans-serif;font-weight:300;font-size:20px;line-height:32px;color:#888}
.badge{top:307px;width:134px;height:58px;background:var(--red)}

.footer{top:3481px;left:0;width:1200px;height:148px;background:var(--footer)}
.footer .name{left:100px;top:64px;display:flex;align-items:center;gap:12px;font-size:12px;color:#ccc}
.footer .name .mark{width:26px;height:26px;border-radius:50%;background:var(--red)}
.footer .social{right:166px;top:68px;display:flex;gap:20px}
.footer .social .dot{width:16px;height:16px;background:#fff}
.base{top:3629px;left:0;width:1200px;height:80px;background:var(--footer-base)}
.base .copy{left:100px;top:40px;font-size:9px;color:#555}
.base .mini{right:144px;top:38px;font-size:9px;font-weight:700;letter-spacing:1px;color:#bbb}
</style>
</head>
<body>

<div class="abs topbar">
  <div class="abs links"><span>ABOUT</span><span>CONTACT</span><span>SERVICES</span></div>
  <div class="abs social"><div class="dot"></div><div class="dot"></div><div class="dot"></div></div>
</div>

<header class="abs header">
  <div class="abs brand"><span class="mark"></span>BRIVOLN</div>
  <span class="abs nav active" style="left:454px">HOME</span>
  <span class="abs nav" style="left:540px">ABOUT</span>
  <span class="abs nav" style="left:632px">SERVICES</span>
  <span class="abs nav" style="left:746px">COMPANY</span>
  <span class="abs nav" style="left:861px">CAREERS</span>
  <span class="abs nav" style="left:969px">CONTACT</span>
  <div class="abs search"></div>
</header>

<section class="abs hero" role="img" aria-label="Aerial view of a city skyline along a lakeshore at sunset">
  <h1 class="abs center">Driven to deliver</h1>
  <p class="abs center">You've never meet management consultants like us.</p>
  <div class="abs btn-red">TAKE A LOOK AT OUR SERVICES</div>
</section>

<div class="abs card-img" style="left:115px;background:linear-gradient(135deg,#e8e8e8,#9a9a9a 60%,#2a2a2e)" role="img" aria-label="Board members meeting around a laptop"></div>
<div class="abs card-img" style="left:448px;background:linear-gradient(160deg,#bcd8ec,#6f98bf 50%,#3b4f6b)" role="img" aria-label="Business charts on a desk with people in an office"></div>
<div class="abs card-img" style="left:781px;background:linear-gradient(135deg,#2a2a2e,#8c8c90 50%,#d9d9d9)" role="img" aria-label="Team joining hands in a circle"></div>
<div class="abs card-title" style="left:115px">Board</div>
<div class="abs card-title" style="left:448px">Management</div>
<div class="abs card-title" style="left:781px">Teams</div>
<p class="abs card-text" style="left:115px">Lorem ipsum dolor sit amet, consectetur adipisicing elit, sed do eiusmod tempor</p>
<p class="abs card-text" style="left:448px">Incididunt ut labore et dolore magna aliqua. Ut enim ad minim veniam, strud.</p>
<p class="abs card-text" style="left:781px">Rexercitation ullamco laboris nisi ut aliquip ex ea commodo consequat.</p>

<section class="abs features">
  <h2 class="abs center">Success through partnerships, achievement through people.</h2>
  <p class="abs center lead">Lorem ipsum dolor sit amet, consectetur adipisicing elit, sed do eiusmod tempor<br>incididunt ut labore et dolore magna aliqua. Ut enim ad minim veniam, quis.</p>

  <div class="abs feature" style="left:116px;top:300px">
    <svg width="48" height="44" viewBox="0 0 48 44" fill="var(--icon)"><rect x="6" y="4" width="3" height="38"/><path d="M10 6c8-4 14 4 22 0s10-2 10-2v20s-4-2-10 1-14-4-22 0z"/></svg>
    <h3>Consultation</h3>
    <p>Lorem ipsum dolor sit amet, consectetur adipisicing elit, sed do eiusmod tempor.</p>
  </div>
  <div class="abs feature" style="left:449px;top:300px">
    <svg width="52" height="44" viewBox="0 0 52 44" fill="var(--icon)"><path d="M2 4h3v34h45v3H2z"/><path d="M8 36V22l10-10 8 8 8-6 14 10v12z"/></svg>
    <h3>Reporting &amp; Analisys</h3>
    <p>Lorem ipsum dolor sit amet, consectetur adipisicing elit, sed do eiusmod tempor.</p>
  </div>
  <div class="abs feature" style="left:782px;top:300px">
    <svg width="48" height="44" viewBox="0 0 48 44" fill="var(--icon)"><path d="M24 4C12 4 4 12 4 20c3-3 6-3 8 0 3-3 7-3 10 0V36c0 3-4 3-4 0h-3c0 7 10 7 10 0V20c3-3 7-3 10 0 2-3 5-3 8 0 0-8-8-16-19-16z"/></svg>
    <h3>Management</h3>
    <p>Lorem ipsum dolor sit amet, consectetur adipisicing elit, sed do eiusmod tempor.</p>
  </div>
  <div class="abs feature" style="left:116px;top:554px">
    <svg width="48" height="44" viewBox="0 0 48 44" fill="var(--icon)"><path d="M17 6h14v6h-3V9h-8v3h-3z"/><rect x="2" y="12" width="44" height="28" rx="4"/><rect x="12" y="12" width="3" height="28" fill="#f5f5f6"/><rect x="33" y="12" width="3" height="28" fill="#f5f5f6"/></svg>
    <h3>Some Other Feature</h3>
    <p>Lorem ipsum dolor sit amet, consectetur adipisicing elit, sed do eiusmod tempor.</p>
  </div>
  <div class="abs feature" style="left:449px;top:554px">
    <svg width="52" height="44" viewBox="0 0 52 44" fill="var(--icon)"><path d="M26 2 4 12v4h44v-4z"/><rect x="8" y="18" width="5" height="16"/><rect x="17" y="18" width="5" height="16"/><rect x="30" y="18" width="5" height="16"/><rect x="39" y="18" width="5" height="16"/><rect x="4" y="36" width="44" height="5"/></svg>
    <h3>Epic Title</h3>
    <p>Lorem ipsum dolor sit amet, consectetur adipisicing elit, sed do eiusmod tempor.</p>
  </div>
  <div class="abs feature" style="left:782px;top:554px">
    <svg width="48" height="44" viewBox="0 0 48 44"><circle cx="24" cy="22" r="17" fill="none" stroke="var(--icon)" stroke-width="4"/><path d="M24 12v11h-8" fill="none" stroke="var(--icon)" stroke-width="4"/></svg>
    <h3>Implementation</h3>
    <p>Lorem ipsum dolor sit amet, consectetur adipisicing elit, sed do eiusmod tempor.</p>
  </div>
</section>

<section class="abs about-band" role="img" aria-label="Hazy city towers and a spire at sunrise">
  <h2 class="abs">Brivoln Consulting</h2>
  <h4 class="abs">Design a Website for Brivoln Consulting</h4>
  <p class="abs">Lorem ipsum dolor sit amet, consectetur adipisicing elit, sed do eiusmod tempor incididunt ut labore et dolore magna aliqua. Ut enim ad minim veniam, quis nostrud exercitation ullamco laboris nisi ut aliquip consequat.</p>
  <div class="abs call">
    <svg width="14" height="22" viewBox="0 0 14 22"><rect x="1" y="1" width="12" height="20" rx="2" fill="none" stroke="var(--red)" stroke-width="2"/><rect x="4" y="16" width="6" height="2" fill="var(--red)"/></svg>
    <div><strong>Call us now!</strong><span>+1 555 0142 | contact@brivoln.com</span></div>
  </div>
</section>

<section class="abs cta">
  <h2 class="abs center">We Make It Our Business<br>To Understand Your Business</h2>
  <div class="abs btn-ghost">KNOW MORE ABOUT US</div>
  <div class="abs btn-red">GET IN TOUCH</div>
</section>

<section class="abs partners">
  <h5 class="abs center">OUR PARTNERS</h5>
  <div class="abs rule"></div>
  <p class="abs center">The design needs to be clean and user friendly with a sharp and professional look.<br>Some examples of great sites we like are:</p>
  <div class="abs badge" style="left:150px"></div>
  <div class="abs badge" style="left:329px"></div>
  <div class="abs badge" style="left:507px"></div>
  <div class="abs badge" style="left:686px"></div>
  <div class="abs badge" style="left:864px"></div>
</section>

<footer class="abs footer">
  <div class="abs name"><span class="mark"></span>Brivoln Consulting</div>
  <div class="abs social"><div class="dot"></div><div class="dot"></div><div class="dot"></div><div class="dot"></div><div class="dot"></div></div>
</footer>
<div class="abs base">
  <div class="abs copy">© 2016 Brivoln Consulting All Rights Reserved.</div>
  <div class="abs mini">BRIVOLN</div>
</div>

</body>
</html>
```